Business Card For Life Coaching Business For Men

Take my existing logo and apply it to a business card. I would like the logo to be prominent with stylistic text below reading Life Coaching For Men. Contact info should show as:
Dale Hartwig
dale@steadforgepath.com

```html
<!DOCTYPE html>
<html lang="en">
<head>
<meta charset="utf-8">
<title>Steadforge Path – Business Card</title>
<link href="https://fonts.googleapis.com/css2?family=Barlow+Condensed:wght@500;600;700&display=swap" rel="stylesheet">
<style>
  :root {
    --backdrop: #d2d3d5;
    --card: #ffffff;
    --navy: #2b2a7f;
    --teal: #0a807c;
    --steel: #7a97b5;
    --mark-faint: #e6e4f1;
  }
  * { box-sizing: border-box; margin: 0; padding: 0; }
  html, body {
    width: 900px; height: 1200px; overflow: hidden;
    background: var(--backdrop);
    font-family: "Barlow Condensed", "Arial Narrow", sans-serif;
  }
  .card {
    position: absolute; left: 133px; width: 632px; height: 364px;
    background: var(--card); overflow: hidden;
  }
  .card--front { top: 210px; }
  .card--back { top: 624px; }

  .brand-dot { position: absolute; border-radius: 50%; background: var(--steel); }
  .card--front .brand-dot { left: 138px; top: 110px; width: 140px; height: 140px; }
  .card--back .brand-dot { left: 32px; top: 45px; width: 90px; height: 90px; }

  .brand-name {
    position: absolute; color: var(--navy); font-weight: 700;
    text-transform: uppercase; line-height: 0.95; letter-spacing: 0.5px;
  }
  .card--front .brand-name { left: 308px; top: 118px; font-size: 56px; }
  .card--back .brand-name { left: 135px; top: 50px; font-size: 36px; }

  .tagline {
    position: absolute; left: 309px; top: 250px;
    color: var(--navy); font-weight: 600; font-size: 17px; letter-spacing: 1.6px;
  }

  .faint-mark {
    position: absolute; left: 320px; top: 20px; width: 330px; height: 330px;
    border-radius: 50%; background: var(--mark-faint);
  }

  .contact { position: absolute; left: 134px; top: 212px; }
  .contact__name { color: var(--teal); font-weight: 700; font-size: 24px; letter-spacing: 0.5px; line-height: 1; }
  .contact__role { color: var(--navy); font-weight: 500; font-size: 16px; margin-top: 4px; }
  .contact__list { list-style: none; margin-top: 10px; }
  .contact__item {
    display: flex; align-items: center; gap: 10px;
    color: var(--navy); font-weight: 500; font-size: 17px; height: 23px;
  }
  .contact__item svg { width: 14px; height: 14px; flex: none; }
</style>
</head>
<body>
  <section class="card card--front">
    <div class="brand-dot"></div>
    <div class="brand-name">Steadforge<br>Path</div>
    <div class="tagline">LIFE COACHING FOR MEN</div>
  </section>

  <section class="card card--back">
    <div class="faint-mark"></div>
    <div class="brand-dot"></div>
    <div class="brand-name">Steadforge<br>Path</div>

    <div class="contact">
      <div class="contact__name">DALE HARTWIG</div>
      <div class="contact__role">Owner</div>
      <ul class="contact__list">
        <li class="contact__item">
          <svg viewBox="0 0 16 16"><path fill="#0a807c" d="M3.5 1l2.5 3-1.4 1.8c.9 2 2.6 3.7 4.6 4.6L11 9l3 2.5-1.5 2.8C6.5 14 2 9.5 1 3z"/></svg>
          (555)014-2290
        </li>
        <li class="contact__item">
          <svg viewBox="0 0 16 16"><rect x="1" y="3" width="14" height="10" fill="#0a807c"/><path d="M1 3l7 6 7-6" fill="none" stroke="#fff" stroke-width="1.3"/></svg>
          dale@steadforgepath.com
        </li>
        <li class="contact__item">
          <svg viewBox="0 0 16 16" fill="none" stroke="#0a807c" stroke-width="1.4"><circle cx="8" cy="8" r="6.5"/><ellipse cx="8" cy="8" rx="2.8" ry="6.5"/><path d="M1.5 8h13M2.5 5h11M2.5 11h11"/></svg>
          www.steadforgepath.com
        </li>
      </ul>
    </div>
  </section>
</body>
</html>
```